New Business Card & Logo Design Project for PR Agency

Halvery & Partners Tech Public Relations agency is looking for a new business card design. Please see our website at www.halvery-pr.example for a description of our services. The design does not necessarily have to match the website’s aesthetic as we are looking for something fresh and modern that reflects our business. We want to emphasize that our focus is on media & public relations, content creation, social media and SEO. We want the business card to convey our BtoB technology focus and should have a very clean look. You are welcome to draw from our current halvery & partners logo on the card or play with that design too. We also like the idea of utilizing blue and white, which are often used in technology-related designs and layouts.
Attached are jpegs of the current logo and current card design for your reference.
Target Market(s)
Our clients are Business-to-Business technology providers.We sell our services to the CEO/President/Marketing director of a technology providing company.
Industry/Entity Type
Business
Look and feel

```html
<!DOCTYPE html>
<html lang="en">
<head>
<meta charset="utf-8">
<title>Halvery &amp; Partners — Business Card</title>
<link href="https://fonts.googleapis.com/css2?family=Cabin:wght@400;600;700&display=swap" rel="stylesheet">
<style>
  :root {
    --backdrop: #e5e6e8;
    --card-white: #ffffff;
    --brand-blue: #1a84c6;
    --band-blue: #0a7cc0;
    --band-glow: #3a9ad6;
    --text-light: #ffffff;
    --shadow: rgba(0, 0, 0, 0.45);
  }
  * { margin: 0; padding: 0; box-sizing: border-box; }
  html, body {
    width: 1200px; height: 1000px; overflow: hidden;
    background: var(--backdrop);
    font-family: "Cabin", sans-serif;
  }
  .business-card {
    position: absolute; left: 134px; top: 231px;
    width: 877px; height: 506px;
    background: var(--card-white);
    box-shadow: 4px 4px 5px var(--shadow);
  }
  .brand-area { position: absolute; left: 0; top: 0; width: 100%; height: 290px; }
  .brand-mark {
    position: absolute; left: 72px; top: 114px;
    display: flex; align-items: center; gap: 18px;
  }
  .brand-dot {
    width: 50px; height: 50px; border-radius: 50%;
    background: var(--brand-blue);
  }
  .brand-name {
    font-size: 54px; font-weight: 700; color: var(--brand-blue);
    letter-spacing: -0.5px; line-height: 1;
  }
  .contact-band {
    position: absolute; left: 0; top: 290px; width: 100%; height: 216px;
    background: radial-gradient(circle at 46% 55%, var(--band-glow) 0%, var(--band-blue) 55%, #0577bb 100%);
    color: var(--text-light);
  }
  .company-block { position: absolute; left: 55px; top: 50px; }
  .company-name { font-size: 31px; font-weight: 700; line-height: 1; margin-bottom: 12px; }
  .address-line { font-size: 19px; line-height: 27px; }
  .person-block { position: absolute; right: 53px; top: 12px; text-align: right; }
  .person-name, .person-role { font-size: 22px; font-weight: 700; line-height: 25px; }
  .contact-list { list-style: none; margin-top: 12px; }
  .contact-list li {
    font-size: 19px; line-height: 23px;
    display: flex; justify-content: flex-end; align-items: center; gap: 6px;
  }
  .contact-list li.gap-before { margin-top: 9px; }
  .contact-icon { width: 16px; height: 16px; }
</style>
</head>
<body>
  <div class="business-card">
    <section class="brand-area">
      <div class="brand-mark">
        <span class="brand-dot"></span>
        <span class="brand-name">halvery &amp; partners</span>
      </div>
    </section>

    <section class="contact-band">
      <div class="company-block">
        <p class="company-name">halvery&amp;partners</p>
        <p class="address-line">48 Harbor Lane</p>
        <p class="address-line">Suite 3 Millbrook</p>
        <p class="address-line">Connecticut 06000</p>
      </div>

      <div class="person-block">
        <p class="person-name">Daniel Reyes</p>
        <p class="person-role">Partner</p>
        <ul class="contact-list">
          <li>
            <svg class="contact-icon" viewBox="0 0 16 16" aria-label="Phone"><path d="M4 1h3l1 4-2 1.5c.8 1.8 2 3 3.5 3.5L11 8l4 1v3c0 1-1 2-2 2C7 14 2 9 2 3c0-1 1-2 2-2z" fill="#fff"/></svg>
            <span>555 014 2290</span>
          </li>
          <li>
            <svg class="contact-icon" viewBox="0 0 16 16" aria-label="Fax"><rect x="4" y="1" width="8" height="5" fill="none" stroke="#fff" stroke-width="1.5"/><rect x="1.5" y="6" width="13" height="6" rx="1.5" fill="#fff"/><rect x="4" y="10" width="8" height="5" fill="#fff" stroke="#0a7cc0" stroke-width="1"/></svg>
            <span>555 014 2725</span>
          </li>
          <li class="gap-before">
            <svg class="contact-icon" viewBox="0 0 16 16" aria-label="Email"><rect x="1" y="3" width="14" height="10" rx="1.5" fill="none" stroke="#fff" stroke-width="1.6"/><path d="M1.5 4l6.5 5 6.5-5" fill="none" stroke="#fff" stroke-width="1.6"/></svg>
            <span>dreyes@halvery-pr.example</span>
          </li>
          <li>
            <svg class="contact-icon" viewBox="0 0 16 16" aria-label="Website"><circle cx="8" cy="8" r="6.5" fill="none" stroke="#fff" stroke-width="1.5"/><ellipse cx="8" cy="8" rx="2.8" ry="6.5" fill="none" stroke="#fff" stroke-width="1.2"/><path d="M1.5 8h13" stroke="#fff" stroke-width="1.2"/></svg>
            <span>www.halvery-pr.example</span>
          </li>
        </ul>
      </div>
    </section>
  </div>
</body>
</html>
```